Professional/modern business card design for construction company

We need a new business card design, double sided keeping it modern, sleek, professional and simple. We are an earthmoving business but do not want any pictures of machinery. I would like one side to have the logo and the other to have all the information, keeping with the colors in our logo. The business card will need to be able to be customised so we can use it for several different managers., we would also like to be able to use the design to apply it to other stationary ie. letterheads, notebooks etc. We do not really have a tag line but we could put on there that we specialise in - Agriculture, Civil Construction and Mining.

Contact Information for Business Card

Brolga Ridge Excavations Pty Ltd
ABN 58 402 937 615
82 Gumleaf Creek Road, Moree NSW 2400

Harold Benton
Managing Director
P 0418 639 204
E haroldbenton@brolgaridgeexc.com.au

Font styles to use
Serif
Sans Serif

Requirements
Nice to have
• I have attached some examples of ideas.
Should not have
• images of machinery

```html
<!DOCTYPE html>
<html lang="en">
<head>
<meta charset="utf-8">
<title>Brolga Ridge Excavations – Business Card</title>
<link href="https://fonts.googleapis.com/css2?family=Open+Sans:wght@400;600;700&display=swap" rel="stylesheet">
<style>
  :root {
    --charcoal: #424242;
    --orange: #f28a1e;
    --white: #ffffff;
    --backdrop: #e9e9e9;
  }
  * { margin: 0; padding: 0; box-sizing: border-box; }
  html, body { width: 1200px; height: 850px; overflow: hidden; }
  body {
    background: var(--backdrop);
    font-family: "Open Sans", Arial, sans-serif;
    display: flex;
    align-items: center;
    justify-content: center;
    gap: 40px;
  }
  .card {
    position: relative;
    width: 540px;
    height: 330px;
    background: var(--white);
    overflow: hidden;
    box-shadow: 0 2px 6px rgba(0,0,0,0.12);
  }

  /* Information side */
  .info-panel {
    position: absolute;
    left: 205px; top: 0; right: 0; bottom: 0;
    background: var(--charcoal);
  }
  .info-notch {
    position: absolute;
    left: 205px; top: 240px;
    width: 70px; height: 90px;
    background: var(--white);
  }
  .side-rule {
    position: absolute;
    left: 26px; top: 175px;
    width: 12px; height: 125px;
    background: var(--charcoal);
  }
  .wordmark {
    position: absolute;
    display: flex;
    align-items: center;
    gap: 8px;
    color: var(--charcoal);
    font-weight: 700;
    text-transform: uppercase;
    line-height: 1.15;
    white-space: nowrap;
  }
  .wordmark-square { background: var(--orange); flex: none; }
  .info-card .wordmark { left: 50px; top: 256px; font-size: 12px; }
  .info-card .wordmark-square { width: 12px; height: 12px; }

  .contact {
    position: absolute;
    left: 232px; top: 48px;
    color: var(--white);
  }
  .contact-name { font-size: 28px; font-weight: 700; line-height: 1; }
  .contact-role { color: var(--orange); font-size: 12px; font-weight: 600; margin-top: 4px; }
  .contact-line { font-size: 11.5px; font-weight: 600; margin-top: 3px; }
  .contact-role + .contact-line { margin-top: 8px; }

  .contact-band {
    position: absolute;
    left: 232px; right: 0;
    height: 28px;
    background: var(--orange);
    color: var(--white);
    display: flex;
    align-items: center;
    gap: 10px;
    padding-left: 14px;
    font-size: 12px;
    font-weight: 600;
  }
  .band-phone { top: 168px; }
  .band-email { top: 206px; left: 180px; padding-left: 66px; }
  .band-icon { width: 16px; height: 16px; flex: none; }

  /* Logo side */
  .logo-card .wordmark {
    left: 0; right: 0; top: 0; bottom: 0;
    justify-content: center;
    font-size: 26px;
    gap: 12px;
  }
  .logo-card .wordmark-square { width: 20px; height: 20px; }
  .accent-bar {
    position: absolute;
    width: 48px; height: 13px;
    background: var(--orange);
  }
  .accent-top { right: 0; top: 62px; }
  .accent-bottom { left: 0; bottom: 62px; }
</style>
</head>
<body>

  <section class="card info-card">
    <div class="info-panel"></div>
    <div class="info-notch"></div>
    <div class="side-rule"></div>
    <div class="wordmark">
      <span class="wordmark-square"></span>
      <span>Brolga Ridge<br>Excavations Pty Ltd</span>
    </div>

    <div class="contact">
      <p class="contact-name">Harold Benton</p>
      <p class="contact-role">Managing Director</p>
      <p class="contact-line">ABN 58 402 937 615</p>
      <p class="contact-line">82 Gumleaf Creek Road, Moree NSW 2400</p>
    </div>

    <div class="contact-band band-phone">
      <svg class="band-icon" viewBox="0 0 16 16" aria-hidden="true">
        <circle cx="8" cy="8" r="8" fill="#ffffff"/>
        <path d="M5.2 4.2l1.3-.2.8 1.9-.9.7c.4.9 1.1 1.6 2 2l.7-.9 1.9.8-.2 1.3c-.1.4-.5.7-.9.6C7.6 10.1 5.9 8.4 5.6 5.1c0-.4.2-.8.6-.9z" fill="#f28a1e"/>
      </svg>
      <span>0418 639 204</span>
    </div>
    <div class="contact-band band-email">
      <svg class="band-icon" viewBox="0 0 16 16" aria-hidden="true">
        <circle cx="8" cy="8" r="8" fill="#ffffff"/>
        <rect x="4" y="5" width="8" height="6" fill="#f28a1e"/>
        <path d="M4 5l4 3.2L12 5" fill="none" stroke="#ffffff" stroke-width="1"/>
      </svg>
      <span>haroldbenton@brolgaridgeexc.com.au</span>
    </div>
  </section>

  <section class="card logo-card">
    <span class="accent-bar accent-top"></span>
    <span class="accent-bar accent-bottom"></span>
    <div class="wordmark">
      <span class="wordmark-square"></span>
      <span>Brolga Ridge Excavations</span>
    </div>
  </section>

</body>
</html>
```